Business card for Bright Keystone

Front (space for each) - Name, title, qualifications, mobile number, email address, website, name/logo,
Back - Business name/logo and slogan "Your key to a first home" underneath,
in small writing underneath need ABN number, CRN number, ACL number
Target Market(s)
First Home Buyers
Industry/Entity Type
Finance
Contact Information for Business Card
Requirements
Must have
- Front (space for each) - Name, title, qualifications, mobile number, email address, website, name/logo,

```html
<!DOCTYPE html>
<html lang="en">
<head>
<meta charset="utf-8">
<title>Bright Keystone – Business Card</title>
<link href="https://fonts.googleapis.com/css2?family=Poppins:ital,wght@0,400;0,500;0,600;1,500&display=swap" rel="stylesheet">
<style>
  :root {
    --page: #2a2a2c;
    --card: #1b1b1c;
    --white: #ffffff;
    --muted: #8c8c8e;
    --rule: #3a3a3c;
    --teal: #19b9a0;
    --green: #7fcf4f;
  }
  * { box-sizing: border-box; margin: 0; padding: 0; }
  html, body { width: 1200px; height: 1200px; overflow: hidden; }
  body {
    background: var(--page);
    font-family: "Poppins", sans-serif;
    color: var(--white);
    position: relative;
  }
  .card {
    position: absolute;
    left: 130px;
    width: 940px;
    height: 440px;
    background: var(--card);
    overflow: hidden;
    box-shadow: 0 20px 40px rgba(0,0,0,.45);
  }
  .card--back { top: 120px; }
  .card--front { top: 640px; }

  .wordmark__name {
    font-weight: 600;
    text-transform: uppercase;
    letter-spacing: 4px;
    line-height: 1.05;
    color: var(--white);
  }

  /* back */
  .card--back .wordmark {
    position: absolute; left: 0; right: 0; top: 128px;
    text-align: center;
  }
  .card--back .wordmark__name { font-size: 50px; }
  .tagline {
    position: absolute; left: 0; right: 0; top: 262px;
    text-align: center;
    font-style: italic; font-weight: 500;
    font-size: 20px;
    color: var(--green);
  }
  .rule {
    position: absolute; top: 276px; height: 1px; background: var(--rule);
  }
  .rule--left { left: 0; width: 290px; }
  .rule--right { right: 0; width: 290px; }
  .registrations {
    position: absolute; left: 0; right: 0; top: 360px;
    display: flex; justify-content: center; gap: 22px;
    font-size: 14px; color: var(--muted); letter-spacing: .5px;
  }

  /* front */
  .card--front .wordmark {
    position: absolute; left: 80px; top: 150px;
  }
  .card--front .wordmark__name { font-size: 46px; }
  .divider {
    position: absolute; left: 0; top: 0;
  }
  .contact {
    position: absolute; left: 530px; top: 95px; width: 370px;
  }
  .contact__name { font-size: 30px; font-weight: 600; letter-spacing: 1px; line-height: 1.1; }
  .contact__title { font-size: 21px; font-weight: 400; letter-spacing: 1px; margin-top: 4px; }
  .contact__quals { font-size: 21px; font-weight: 500; letter-spacing: 1px; color: var(--green); margin-top: 2px; }
  .contact__rule { height: 1px; background: var(--rule); margin: 16px 0 14px; }
  .contact__list { list-style: none; }
  .contact__item {
    display: flex; align-items: center; gap: 14px;
    font-size: 21px; margin-bottom: 8px; letter-spacing: .3px;
  }
  .contact__icon { width: 24px; height: 24px; flex: none; }
</style>
</head>
<body>

<section class="card card--back" aria-label="Card back">
  <div class="wordmark">
    <span class="wordmark__name">Bright<br>Keystone</span>
  </div>
  <div class="rule rule--left"></div>
  <p class="tagline">Your key to a first home</p>
  <div class="rule rule--right"></div>
  <p class="registrations">
    <span>ABN 5082913</span><span>|</span>
    <span>CRN 64071538</span><span>|</span>
    <span>ACL BK70416</span>
  </p>
</section>

<section class="card card--front" aria-label="Card front">
  <svg class="divider" width="940" height="440" aria-hidden="true">
    <line x1="470" y1="40" x2="350" y2="400" stroke="var(--teal)" stroke-width="1.5"/>
  </svg>
  <div class="wordmark">
    <span class="wordmark__name">Bright<br>Keystone</span>
  </div>
  <div class="contact">
    <h1 class="contact__name">DANIEL MARSH</h1>
    <p class="contact__title">CEO/FOUNDER</p>
    <p class="contact__quals">MY QUALIFICATIONS</p>
    <div class="contact__rule"></div>
    <ul class="contact__list">
      <li class="contact__item">
        <svg class="contact__icon" viewBox="0 0 24 24" aria-hidden="true"><rect x="6" y="2" width="12" height="20" rx="2" fill="none" stroke="var(--teal)" stroke-width="2"/><line x1="10" y1="18" x2="14" y2="18" stroke="var(--teal)" stroke-width="2"/></svg>
        214-555-0187
      </li>
      <li class="contact__item">
        <svg class="contact__icon" viewBox="0 0 24 24" aria-hidden="true"><rect x="2" y="5" width="20" height="14" fill="none" stroke="var(--green)" stroke-width="2"/><polyline points="2,5 12,13 22,5" fill="none" stroke="var(--green)" stroke-width="2"/></svg>
        dan@brightkeystone.com
      </li>
      <li class="contact__item">
        <svg class="contact__icon" viewBox="0 0 24 24" aria-hidden="true"><g fill="none" stroke="var(--teal)" stroke-width="1.8"><circle cx="12" cy="12" r="10"/><ellipse cx="12" cy="12" rx="4.5" ry="10"/><line x1="2" y1="12" x2="22" y2="12"/><line x1="4" y1="7" x2="20" y2="7"/><line x1="4" y1="17" x2="20" y2="17"/></g></svg>
        www.brightkeystone.com
      </li>
    </ul>
  </div>
</section>

</body>
</html>
```